Business card design for web travel company

Hi
we'd like to receive some proposal for a business card design.
Quindra is a private travel club, dedicated to all travel lovers, with unique offers for exclusive destinations all around the world. At Quindra you can find a wide range of offers for resorts, boutique hotels and travel packages at the best guaranteed price available on the market. The convenience of the offer is guaranteed by a private sales model: offers are available for a limited time only and they are personally chosen by Quindra's qualified team of travel experts.
We offer only exclusive hotels with discounted prices but we are not an outlet or a discount supermarket: the design should reflect our connection with luxury, exclusivity using the same style of our website www.quindra-example.com.
We want to make sure that when we'll present ourself to our business partner they will feel immediately which is our brand positioning giving them also a sense of an affordable and reliable partner.
In attachment you can also find our brand guidelines (please note that we are NOT USING ANY MORE THE TAG LINE "Five star outlet" mentioned in it).
The info to be inserted are:
Name Surname
Job Title
Tel
Mobile (when needed)
Email
Quindra S.r.l.
Via Pietro Lanzi 27
20137 Milano

```html
<!DOCTYPE html>
<html lang="en">
<head>
<meta charset="utf-8">
<title>Quindra Business Card</title>
<link href="https://fonts.googleapis.com/css2?family=Source+Sans+3:wght@300;400;600&display=swap" rel="stylesheet">
<style>
  :root {
    --backdrop: #d9d6d3;
    --card: #262626;
    --card-edge: #1b1b1b;
    --card-shade: #2e2e2e;
    --ink-light: #f2f2f2;
    --ink-soft: #cfcfcf;
    --gold: #d8c89a;
  }
  * { margin: 0; padding: 0; box-sizing: border-box; }
  html, body { width: 1200px; height: 1189px; overflow: hidden; }
  body {
    background: var(--backdrop);
    font-family: "Source Sans 3", "Myriad Pro", sans-serif;
    position: relative;
  }
  .card {
    position: absolute;
    background: linear-gradient(160deg, var(--card-shade), var(--card) 60%, var(--card-edge));
    box-shadow: 0 6px 18px rgba(0,0,0,0.35);
  }
  .card--front { left: 50px; top: 250px; width: 545px; height: 330px; }
  .card--back  { left: 605px; top: 250px; width: 545px; height: 330px; }
  .card--info-under { left: 240px; top: 700px; width: 590px; height: 340px; background: var(--card-edge); }
  .card--info { left: 210px; top: 680px; width: 590px; height: 340px; }

  .wordmark {
    position: absolute;
    color: var(--ink-light);
    font-weight: 300;
    letter-spacing: 1px;
  }
  .card--front .wordmark { left: 175px; top: 132px; font-size: 46px; }
  .front-url {
    position: absolute; left: 195px; top: 200px;
    color: var(--ink-soft); font-size: 17px; font-weight: 300; letter-spacing: 3.5px;
  }
  .back-url {
    position: absolute; right: 28px; bottom: 26px;
    color: var(--ink-light); font-size: 18px; font-weight: 400;
  }

  .card--info .wordmark { left: 80px; top: 148px; font-size: 36px; }
  .divider {
    position: absolute; left: 285px; top: 35px; width: 2px; height: 270px;
    background: linear-gradient(to bottom, transparent, #e8e8e8 55%, transparent);
  }
  .details { position: absolute; left: 335px; top: 60px; color: var(--ink-soft); }
  .details__name { color: var(--gold); font-size: 21px; font-weight: 600; }
  .details__title { font-size: 16px; font-weight: 300; margin-top: 2px; }
  .details__address { font-size: 14px; font-weight: 300; line-height: 19px; margin-top: 32px; }
  .details__contacts { list-style: none; font-size: 14px; font-weight: 300; margin-top: 10px; }
  .details__contacts li { display: flex; align-items: center; gap: 10px; height: 21px; }
  .details__contacts svg { width: 16px; height: 14px; fill: var(--ink-soft); }
</style>
</head>
<body>
  <section class="card card--front">
    <div class="wordmark">Quindra</div>
    <div class="front-url">www.quindra-example.com</div>
  </section>

  <section class="card card--back">
    <div class="back-url">www.quindra-example.com</div>
  </section>

  <div class="card card--info-under"></div>
  <section class="card card--info">
    <div class="wordmark">Quindra</div>
    <div class="divider"></div>
    <div class="details">
      <div class="details__name">Marco Ventrelli</div>
      <div class="details__title">Marketing Manager</div>
      <div class="details__address">Quindra S.r.l.<br>Via Pietro Lanzi 27<br>20137 Milano</div>
      <ul class="details__contacts">
        <li>
          <svg viewBox="0 0 16 14"><path d="M1 5c0-2 3-3 7-3s7 1 7 3v1h-4V4.5C10 4 6 4 5 4.5V6H1z"/><rect x="3" y="7" width="10" height="6" rx="1"/></svg>
          02 555 0148
        </li>
        <li>
          <svg viewBox="0 0 16 14"><rect x="1" y="10" width="2" height="4"/><rect x="5" y="7" width="2" height="7"/><rect x="9" y="4" width="2" height="10"/><rect x="13" y="1" width="2" height="13"/></svg>
          02 555 0149
        </li>
        <li>
          <svg viewBox="0 0 16 14"><path d="M1 2h14v10H1z M2.5 3.5 8 8l5.5-4.5v7h-11z" fill-rule="evenodd"/></svg>
          info@quindra-example.com
        </li>
      </ul>
    </div>
  </section>
</body>
</html>
```